Crestfield Slab & Tile Needs a Business Card

Attached you will find your logo, my photo and design guidelines for a new business card. The final design will need two separate files to create an embossed card. The cards will be printed by www.plimbo.com (Instructions below)
Format is the Plimbo SQUARE card
Crestfield Slab And Tile is a brick and mortar, retail stone and tile shop.
One the front:
Crestfield Slab And Tile
Gerald Pennock
Owner
48207 Dunmore Ridge Blvd
Suite R & T
Larkspur Hollow, NC 28190
Cell: 704-555-0183
Web: www.CrestfieldSlabAndTile.com
(Make each word of the domain a different or alternating color)
On the back;
Something that shows beautiful colorful tile
Follow the design guide closely please. For more information see this page that describes creating the spot gloss file: https://www.plimbo.com/us/business-cards/design-guidelines-spot-gloss
The logo is what we would like to have raised spot glossed.
Contact Information for Business Card
Format is the Plimbo SQUARE card. See attahced guidlines.

```html
<!DOCTYPE html>
<html lang="en">
<head>
<meta charset="utf-8">
<title>Crestfield Slab &amp; Tile – Business Card</title>
<link rel="stylesheet" href="https://fonts.googleapis.com/css2?family=Cormorant+Garamond:wght@500;600&family=Montserrat:wght@500;600;700&display=swap">
<style>
  :root {
    --backdrop: #ececec;
    --navy: #2c3845;
    --navy-deep: #1f2933;
    --navy-soft: #3a4858;
    --rust: #b8471f;
    --gold: #c98f2a;
    --sage: #8a9477;
    --paper: #ffffff;
    --ink: #1f2933;
  }
  * { box-sizing: border-box; margin: 0; padding: 0; }
  html, body { width: 1200px; height: 900px; overflow: hidden; }
  body { background: var(--backdrop); position: relative; font-family: "Montserrat", sans-serif; }

  .card { position: absolute; top: 219px; width: 460px; height: 460px; overflow: hidden; }

  .brand-name, .brand-sub {
    font-family: "Cormorant Garamond", serif; font-weight: 600;
    text-transform: uppercase; white-space: nowrap; line-height: 1;
  }

  /* Back side */
  .card-back { left: 112px; background: var(--navy); }
  .back-square {
    position: absolute; left: 142px; top: 100px; width: 176px; height: 176px;
    background: var(--navy-soft);
  }
  .back-wordmark {
    position: absolute; left: 82px; width: 296px; top: 283px; text-align: center;
    color: var(--navy-deep);
  }
  .back-wordmark .brand-name { font-size: 40px; letter-spacing: 4px; }
  .back-wordmark .brand-rule { height: 1px; background: var(--navy-soft); margin: 10px 0 10px; }
  .back-wordmark .brand-sub { font-size: 20px; letter-spacing: 13px; margin-right: -13px; }

  /* Front side */
  .card-front { left: 627px; background: var(--paper); }
  .front-square {
    position: absolute; left: 37px; top: 57px; width: 114px; height: 114px;
    background: var(--navy);
  }
  .front-wordmark {
    position: absolute; left: 172px; width: 251px; top: 92px; text-align: center;
    color: var(--navy);
  }
  .front-wordmark .brand-name { font-size: 33px; letter-spacing: 3px; margin-right: -3px; }
  .front-wordmark .brand-rule { height: 1px; background: var(--gold); margin: 7px 0 10px; }
  .front-wordmark .brand-sub { font-size: 17px; letter-spacing: 10px; margin-right: -10px; }

  .person-name {
    position: absolute; left: 37px; top: 208px;
    font-family: "Cormorant Garamond", serif; font-weight: 600; font-size: 34px; color: var(--ink); letter-spacing: 0.5px;
  }
  .person-role {
    position: absolute; left: 37px; right: 37px; top: 249px; display: flex; align-items: center; gap: 8px;
    color: var(--rust); font-size: 16px; font-weight: 500; letter-spacing: 0.5px;
  }
  .person-role .rule { flex: 1; height: 0; border-top: 2px dashed var(--navy); }

  .portrait {
    position: absolute; left: 37px; top: 282px; width: 133px; height: 133px;
    background: linear-gradient(160deg, #4a5158 0%, #2d3339 70%);
    border-top: 3px solid var(--rust); border-right: 2px solid var(--gold);
  }

  .address {
    position: absolute; right: 37px; top: 278px; text-align: right; font-style: normal;
    font-size: 14.5px; font-weight: 500; color: var(--ink); line-height: 25px;
  }
  .phone {
    position: absolute; right: 37px; top: 370px;
    font-size: 24px; font-weight: 700; letter-spacing: 4.5px; margin-right: -4.5px; color: var(--ink);
  }
  .web {
    position: absolute; right: 37px; top: 400px; font-size: 14px; font-weight: 500; color: var(--ink);
  }
  .web .w1 { color: var(--rust); }
  .web .w2 { color: var(--gold); }
  .web .w3 { color: var(--sage); }

  .tile-band {
    position: absolute; left: 0; right: 0; bottom: 0; height: 28px;
    background: linear-gradient(90deg, var(--navy) 0%, var(--rust) 35%, var(--navy) 55%, var(--gold) 80%, var(--navy) 100%);
  }
</style>
</head>
<body>

<section class="card card-back" aria-label="Card back">
  <div class="back-square"></div>
  <div class="back-wordmark">
    <div class="brand-name">Crestfield</div>
    <div class="brand-rule"></div>
    <div class="brand-sub">Slab &amp; Tile</div>
  </div>
</section>

<section class="card card-front" aria-label="Card front">
  <div class="front-square"></div>
  <div class="front-wordmark">
    <div class="brand-name">Crestfield</div>
    <div class="brand-rule"></div>
    <div class="brand-sub">Slab &amp; Tile</div>
  </div>

  <div class="person-name">Gerald Pennock</div>
  <div class="person-role"><span>Owner</span><span class="rule"></span></div>

  <div class="portrait" role="img" aria-label="Portrait photo of the owner"></div>

  <address class="address">
    48207 Dunmore Ridge Blvd<br>
    Suite R &amp; T<br>
    Larkspur Hollow, NC 28190
  </address>
  <div class="phone">704-555-0183</div>
  <div class="web">www.<span class="w1">Crestfield</span><span class="w2">Slab</span><span class="w3">And</span><span class="w1">Tile</span>.com</div>

  <div class="tile-band" role="img" aria-label="Decorative colourful tile pattern band"></div>
</section>

</body>
</html>
```